mechanical repair shop

our shop repairs light and medium duty trucks

we sell tires , do oil changes, engine and transmissions
vehicle accessories, alignments, brakes , exhaust, all major and minor repairs.

if you would like to get a hold of me email: gideon.marlowe@quillventa.example tel: 1-780-555-0148

Target Market(s)

light and medium duty trucks and cars

Industry/Entity Type

Shop

Colors
f37122

Requirements
Must have
• visual sales displays
Nice to have
• pictures

```html
<!DOCTYPE html>
<html lang="en">
<head>
<meta charset="utf-8">
<title>Quillventa Services Ltd. – Truck Repair Flyer</title>
<link rel="stylesheet" href="https://fonts.googleapis.com/css2?family=Oswald:wght@300;400;500;600&family=Montserrat:ital,wght@0,400;1,400&display=swap">
<style>
  :root {
    --orange: #f37122;
    --orange-deep: #e2561a;
    --black: #0b0b0b;
    --white: #ffffff;
    --ink: #1a1a1a;
  }
  * { margin: 0; padding: 0; box-sizing: border-box; }
  html, body { width: 960px; height: 1200px; overflow: hidden; background: var(--white); }
  .flyer { position: relative; width: 960px; height: 1200px; overflow: hidden; font-family: "Montserrat", sans-serif; color: var(--ink); }
  .backdrop { position: absolute; inset: 0; }

  .brand { position: absolute; left: 52px; top: 118px; width: 250px; }
  .brand-name { font-family: "Oswald", sans-serif; font-weight: 600; font-size: 40px; line-height: 1; color: var(--orange); letter-spacing: 1px; }
  .brand-sub { font-family: "Oswald", sans-serif; font-weight: 400; font-size: 14px; color: var(--white); margin-top: 6px; letter-spacing: .5px; }
  .brand-tag { font-family: "Oswald", sans-serif; font-weight: 400; font-size: 11px; color: var(--orange); letter-spacing: .5px; }

  .photo { position: absolute; }
  .photo-trucks { left: 300px; top: 142px; width: 660px; height: 215px;
    background: linear-gradient(180deg, #fafafa 0%, #e6e6e6 70%, #3a3a3a 100%);
    clip-path: polygon(4% 18%, 100% 0, 100% 100%, 0 100%, 0 40%); }
  .photo-tire { left: 501px; top: 537px; width: 223px; height: 238px;
    background: linear-gradient(160deg, #8d8d8d 0%, #3b3b3b 55%, #1c1c1c 100%); }
  .photo-oil { left: 730px; top: 579px; width: 185px; height: 196px;
    background: linear-gradient(170deg, #c9c9c9 0%, #d9a11d 45%, #7a7a7a 100%); }

  .headline { position: absolute; right: 42px; top: 370px; text-align: right;
    font-family: "Oswald", sans-serif; font-weight: 600; font-size: 45px; line-height: 50px;
    letter-spacing: -1.2px; text-transform: uppercase; color: var(--white); }
  .headline .line-one { margin-right: 32px; }
  .headline .dark { color: var(--black); }

  .services { position: absolute; left: 37px; top: 506px; }
  .services-title { font-family: "Oswald", sans-serif; font-weight: 500; font-size: 40px; color: var(--orange); letter-spacing: -.5px; line-height: 1.1; }
  .service-list { list-style: none; margin-top: 14px; }
  .service-list li { display: flex; align-items: center; gap: 10px; font-size: 15.5px; height: 32.8px; color: var(--ink); }
  .tick { width: 18px; height: 18px; flex: none; }

  .about { position: absolute; left: 498px; top: 795px; width: 422px;
    font-style: italic; font-size: 14.3px; line-height: 24.2px; text-align: justify; color: var(--ink); }

  .contact { position: absolute; left: 38px; top: 1094px; }
  .contact-lead { font-family: "Oswald", sans-serif; font-weight: 400; font-size: 25px; color: var(--orange); letter-spacing: -.3px; }
  .contact-phone { display: flex; align-items: center; gap: 10px; margin-top: 4px;
    font-family: "Oswald", sans-serif; font-weight: 300; font-size: 46px; color: var(--white); line-height: 1; }
  .phone-icon { width: 30px; height: 40px; }

  .website { position: absolute; right: 22px; top: 1106px;
    font-family: "Oswald", sans-serif; font-weight: 300; font-size: 25px; color: var(--white); }
</style>
</head>
<body>
<div class="flyer">
  <svg class="backdrop" width="960" height="1200" viewBox="0 0 960 1200" aria-hidden="true">
    <defs>
      <linearGradient id="orangeSweep" x1="0" y1="0" x2="1" y2="0">
        <stop offset="0" stop-color="var(--orange)"/>
        <stop offset="1" stop-color="var(--orange-deep)"/>
      </linearGradient>
    </defs>
    <rect x="0" y="0" width="960" height="600" fill="var(--black)"/>
    <polygon points="833,0 960,0 0,432" fill="var(--white)"/>
    <polygon points="960,32 960,540 0,430" fill="url(#orangeSweep)"/>
    <polygon points="0,430 960,540 960,600 0,600" fill="var(--white)"/>
    <polygon points="0,430 960,540 960,592" fill="var(--black)"/>
    <polygon points="0,1044 960,1192 960,1200 0,1200" fill="var(--black)"/>
    <polygon points="571,1124 960,1046 960,1192" fill="var(--orange-deep)"/>
  </svg>

  <div class="brand">
    <div class="brand-name">QUILLVENTA</div>
    <div class="brand-sub">Services Ltd.</div>
    <div class="brand-tag">Oilfield Services &amp; Maintenance</div>
  </div>

  <div class="photo photo-trucks" role="img" aria-label="Three white light and medium duty box trucks parked side by side"></div>

  <h1 class="headline">
    <div class="line-one">Your complete <span class="dark">light &amp; medium</span></div>
    <div><span class="dark">duty</span> truck repair facility</div>
  </h1>

  <section class="services">
    <h2 class="services-title">Services We Offer:</h2>
    <ul class="service-list">
      <li><svg class="tick" viewBox="0 0 20 20"><path d="M17 8.5A7.5 7.5 0 1 1 13.5 3.7" fill="none" stroke="var(--orange)" stroke-width="2" stroke-linecap="round"/><path d="M6.5 9.5l3 3 7.5-8" fill="none" stroke="var(--orange)" stroke-width="2" stroke-linecap="round" stroke-linejoin="round"/></svg>Factory recommended service/maintenance</li>
      <li><svg class="tick" viewBox="0 0 20 20"><path d="M17 8.5A7.5 7.5 0 1 1 13.5 3.7" fill="none" stroke="var(--orange)" stroke-width="2" stroke-linecap="round"/><path d="M6.5 9.5l3 3 7.5-8" fill="none" stroke="var(--orange)" stroke-width="2" stroke-linecap="round" stroke-linejoin="round"/></svg>Oil change</li>
      <li><svg class="tick" viewBox="0 0 20 20"><path d="M17 8.5A7.5 7.5 0 1 1 13.5 3.7" fill="none" stroke="var(--orange)" stroke-width="2" stroke-linecap="round"/><path d="M6.5 9.5l3 3 7.5-8" fill="none" stroke="var(--orange)" stroke-width="2" stroke-linecap="round" stroke-linejoin="round"/></svg>Fuel system repair and maintenance</li>
      <li><svg class="tick" viewBox="0 0 20 20"><path d="M17 8.5A7.5 7.5 0 1 1 13.5 3.7" fill="none" stroke="var(--orange)" stroke-width="2" stroke-linecap="round"/><path d="M6.5 9.5l3 3 7.5-8" fill="none" stroke="var(--orange)" stroke-width="2" stroke-linecap="round" stroke-linejoin="round"/></svg>Battery system diagnosis &amp; repair</li>
      <li><svg class="tick" viewBox="0 0 20 20"><path d="M17 8.5A7.5 7.5 0 1 1 13.5 3.7" fill="none" stroke="var(--orange)" stroke-width="2" stroke-linecap="round"/><path d="M6.5 9.5l3 3 7.5-8" fill="none" stroke="var(--orange)" stroke-width="2" stroke-linecap="round" stroke-linejoin="round"/></svg>Check engine light</li>
      <li><svg class="tick" viewBox="0 0 20 20"><path d="M17 8.5A7.5 7.5 0 1 1 13.5 3.7" fill="none" stroke="var(--orange)" stroke-width="2" stroke-linecap="round"/><path d="M6.5 9.5l3 3 7.5-8" fill="none" stroke="var(--orange)" stroke-width="2" stroke-linecap="round" stroke-linejoin="round"/></svg>Electrical problems</li>
      <li><svg class="tick" viewBox="0 0 20 20"><path d="M17 8.5A7.5 7.5 0 1 1 13.5 3.7" fill="none" stroke="var(--orange)" stroke-width="2" stroke-linecap="round"/><path d="M6.5 9.5l3 3 7.5-8" fill="none" stroke="var(--orange)" stroke-width="2" stroke-linecap="round" stroke-linejoin="round"/></svg>Engine performance</li>
      <li><svg class="tick" viewBox="0 0 20 20"><path d="M17 8.5A7.5 7.5 0 1 1 13.5 3.7" fill="none" stroke="var(--orange)" stroke-width="2" stroke-linecap="round"/><path d="M6.5 9.5l3 3 7.5-8" fill="none" stroke="var(--orange)" stroke-width="2" stroke-linecap="round" stroke-linejoin="round"/></svg>Exhaust problems</li>
      <li><svg class="tick" viewBox="0 0 20 20"><path d="M17 8.5A7.5 7.5 0 1 1 13.5 3.7" fill="none" stroke="var(--orange)" stroke-width="2" stroke-linecap="round"/><path d="M6.5 9.5l3 3 7.5-8" fill="none" stroke="var(--orange)" stroke-width="2" stroke-linecap="round" stroke-linejoin="round"/></svg>Tires</li>
      <li><svg class="tick" viewBox="0 0 20 20"><path d="M17 8.5A7.5 7.5 0 1 1 13.5 3.7" fill="none" stroke="var(--orange)" stroke-width="2" stroke-linecap="round"/><path d="M6.5 9.5l3 3 7.5-8" fill="none" stroke="var(--orange)" stroke-width="2" stroke-linecap="round" stroke-linejoin="round"/></svg>30/60/90 K mileage maintenance services</li>
      <li><svg class="tick" viewBox="0 0 20 20"><path d="M17 8.5A7.5 7.5 0 1 1 13.5 3.7" fill="none" stroke="var(--orange)" stroke-width="2" stroke-linecap="round"/><path d="M6.5 9.5l3 3 7.5-8" fill="none" stroke="var(--orange)" stroke-width="2" stroke-linecap="round" stroke-linejoin="round"/></svg>Cooling system repair and maintenance</li>
      <li><svg class="tick" viewBox="0 0 20 20"><path d="M17 8.5A7.5 7.5 0 1 1 13.5 3.7" fill="none" stroke="var(--orange)" stroke-width="2" stroke-linecap="round"/><path d="M6.5 9.5l3 3 7.5-8" fill="none" stroke="var(--orange)" stroke-width="2" stroke-linecap="round" stroke-linejoin="round"/></svg>Air conditioning / heating repair</li>
      <li><svg class="tick" viewBox="0 0 20 20"><path d="M17 8.5A7.5 7.5 0 1 1 13.5 3.7" fill="none" stroke="var(--orange)" stroke-width="2" stroke-linecap="round"/><path d="M6.5 9.5l3 3 7.5-8" fill="none" stroke="var(--orange)" stroke-width="2" stroke-linecap="round" stroke-linejoin="round"/></svg>Brake system</li>
      <li><svg class="tick" viewBox="0 0 20 20"><path d="M17 8.5A7.5 7.5 0 1 1 13.5 3.7" fill="none" stroke="var(--orange)" stroke-width="2" stroke-linecap="round"/><path d="M6.5 9.5l3 3 7.5-8" fill="none" stroke="var(--orange)" stroke-width="2" stroke-linecap="round" stroke-linejoin="round"/></svg>Steering &amp; suspension</li>
    </ul>
  </section>

  <div class="photo photo-tire" role="img" aria-label="Mechanic's gloved hands mounting a truck tire on a tire changer"></div>
  <div class="photo photo-oil" role="img" aria-label="Golden motor oil being poured into an engine filler neck"></div>

  <p class="about">Quillventa Services Ltd. has set up and successfully operates a complete equipment repair facility. First set up to be a dedicated repair shop for a single large client, Quillventa has now expanded to include all manner of clients with diverse equipment needs. With Journeyman and Apprentice HD mechanics available 24 hours a day our facility is ready to handle all of your equipment needs. We are an ‘approved’ repair facility for a growing list of equipment manufacturers including: Torvane, Belwick, Liftora, KRM, Hoistmark etc.</p>

  <div class="contact">
    <div class="contact-lead">Call us for more information</div>
    <div class="contact-phone">
      <svg class="phone-icon" viewBox="0 0 24 32" aria-hidden="true"><path d="M7 2c1.2-.6 2.2 0 2.6 1l2 5c.4 1-.1 1.9-1 2.4l-2 1c-.5.3-.6.8-.5 1.3.9 3.4 2 5.6 3.6 7.7.3.4.9.5 1.3.2l1.8-1.2c.9-.6 2-.4 2.6.5l3 4.4c.6.9.3 2-.6 2.6l-2.3 1.6c-1.6 1.1-3.8 1-5.3-.3C6.4 24.7 3 17.5 2.6 10c-.1-2 1-3.8 2.7-4.8z" fill="var(--white)"/></svg>
      <span>780 555 0172</span>
    </div>
  </div>

  <div class="website">www.quillventa.example</div>
</div>
</body>
</html>
```